Need to design a business card with logo

Hellow
we are a company ,
PT KORAN MELATI JAYA
looking for design of name card.
what we do is property development and management.
design preferable professional corporate look and feel.
corporate. color, pantone colour 289
information required is
company name " Koran Melati Jaya"
person name eg " Peter Walsh"
person title eg "secret agent"
address: 12 heron lane , jakarta, indonesia
phone : +6221 5917264
mobile : 0812 463 518
email : peter@walshmail.example
website: www.peterwa.example
if you want to include logo in the design you are welcome and appreciated , or you can simply use the company name as the logo.
thanks
Target Market(s)
corporate , business person , show events, exhibition events ,etc
Industry/Entity Type
Business
Look and feel
Each slider illustrates characteristics of the customer's brand and the style your logo design should communicate.

```html
<!DOCTYPE html>
<html lang="en">
<head>
<meta charset="UTF-8">
<title>Koran Melati Jaya — Business Card</title>
<link href="https://fonts.googleapis.com/css2?family=Staatliches&family=Tinos&display=swap" rel="stylesheet">
<style>
  :root {
    --navy: #00224f;
    --band: #93aedf;
    --mark: #161b3a;
    --white: #ffffff;
  }
  html, body {
    margin: 0;
    padding: 0;
    overflow: hidden;
    background: var(--navy);
  }
  .card {
    position: relative;
    width: 1200px;
    height: 667px;
    background: var(--navy);
    overflow: hidden;
  }
  .band {
    position: absolute;
    background: var(--band);
  }
  .band--wide-left  { left: 0;     top: 266px; width: 277px; height: 60px; }
  .band--thin-left  { left: 0;     top: 334px; width: 277px; height: 8px; }
  .band--wide-right { left: 930px; top: 266px; width: 270px; height: 60px; }
  .band--thin-right { left: 930px; top: 334px; width: 270px; height: 8px; }
  .brand-dot {
    position: absolute;
    left: 549px;
    top: 161px;
    width: 76px;
    height: 76px;
  }
  .company-name {
    position: absolute;
    left: 277px;
    width: 653px;
    top: 255px;
    margin: 0;
    text-align: center;
    font-family: "Staatliches", "Arial Narrow", sans-serif;
    font-weight: 400;
    font-size: 66px;
    line-height: 1;
    letter-spacing: 0.07em;
    word-spacing: 0.12em;
    color: var(--white);
  }
  .tagline {
    position: absolute;
    left: 277px;
    width: 653px;
    top: 320px;
    margin: 0;
    text-align: center;
    font-family: "Tinos", "Times New Roman", serif;
    font-size: 22px;
    line-height: 1;
    color: var(--white);
  }
</style>
</head>
<body>
  <main class="card">
    <div class="band band--wide-left"></div>
    <div class="band band--thin-left"></div>
    <div class="band band--wide-right"></div>
    <div class="band band--thin-right"></div>

    <svg class="brand-dot" viewBox="0 0 76 76" aria-hidden="true">
      <circle cx="38" cy="38" r="38" fill="var(--mark)"/>
    </svg>

    <h1 class="company-name">Koran Melati Jaya</h1>
    <p class="tagline">Property Development and Management Company</p>
  </main>
</body>
</html>
```